A new website for Electrical Contractor Business

We are looking for a unique and new WordPress website design which would include 5 Pages - Home Page, Meet the Team, Our Services, Our Projects and Contact Us page.

The global theme for the website needs to be professional but simple to navigate as we cater for both business and home owner customers.

Our core business service is targeted around lighting from single room decorative to large office so the theme should incorporate this in some way.

The home page should include;
Our business logo, Contact number, Email address, small Image rotation box - Highlighting pervious projectsText box - With welcome message, chirpnet feed news reel/Customer feed back box.

I would also like to see a 2 boxes for the separate customer types we services. Business and Home Owner. each box will have a small image with a small text description with a link to the area of the services page relevant to that customer type.

Meet the team page -This will be introducing potential customers to the team so I would like it to include for each team member. Something like a small image and text area which will introduce an outline of the team members skills and abilities.

Our Services page This page will be outlining the different services on offer to the both customer types business and homeowner. Each service should have an image with text description of the service would good here.

Our projects page-Will include images of pervious projects and work we have completed along with a text area for the project description/ outliner.

Contact Us page - Should include a contact form which should include an option for the customer to quest us to call them back, also a selection box for them to inform us our how they found our details would be good.

Colour - The theme colours can be taken from the logo or feel free to impress with your own imagination.

Remember we are looking for a website that will interest our customers enough to except our services or be drawn further into the website.. So call to action links to other areas of the site/ contact page are welcome

Target Market(s)

Business - Office, warehousing and Large Store - lighting and Power
Home owner lighting and power

Coding

Coded - Design and coding required

Number of Pages Required

5+ page

Font styles to use
Serif
Sans Serif

Colors

Designer to choose colors to be used in the design.

Requirements
Must have
• Logo integrated into the website design - i.e. website colours which allow the logo to blend into the design.
Nice to have
• Custom but professional theme catering to business customers, but also show that we do provide services to home owners too.
Should not have
• Sorry am not interested in one oversized block image on rotation covering half the home page.. Images will be needed but not a single block over sized frame with not text, shape. Please use your imagination when considering this design

```html
<!DOCTYPE html>
<html lang="en">
<head>
<meta charset="utf-8">
<title>Brightline Electrical – Home</title>
<link href="https://fonts.googleapis.com/css2?family=Titillium+Web:wght@400;600;700&family=Poppins:wght@400;500&display=swap" rel="stylesheet">
<style>
:root{
  --orange:#f26a2d;
  --navy:#1f3260;
  --white:#ffffff;
  --ink:#222428;
  --muted:#4a4d55;
  --pale:#fde9df;
  --dot:#d4d4d4;
}
*{margin:0;padding:0;box-sizing:border-box}
html,body{width:1200px;height:2469px;overflow:hidden}
body{position:relative;background:var(--white);font-family:'Poppins',sans-serif;color:var(--ink)}
.abs{position:absolute}

/* top bar */
.topbar{left:0;top:0;width:1200px;height:41px;background:var(--orange);color:var(--white)}
.topbar .contact{position:absolute;top:0;height:41px;display:flex;align-items:center;gap:10px}
.topbar .phone{left:744px;font-family:'Titillium Web',sans-serif;font-size:21px}
.topbar .email{left:924px;font-size:13px}

/* nav */
.navbar{left:0;top:41px;width:1200px;height:61px;background:var(--white)}
.brand{left:110px;top:6px;display:flex;flex-direction:column;align-items:center;gap:4px}
.brand-mark{width:56px;height:56px;border-radius:50%;background:var(--orange);border:4px solid var(--white)}
.brand-name{font-family:'Titillium Web',sans-serif;font-weight:600;font-size:17px;letter-spacing:1px;color:var(--navy)}
.menu{right:110px;top:41px;height:61px;display:flex;align-items:center;gap:58px;list-style:none;font-family:'Titillium Web',sans-serif;font-size:15px;color:var(--ink)}

/* hero */
.hero{left:0;top:102px;width:1200px;height:468px;background:linear-gradient(115deg,#3b2a1f 0%,#6a4a30 35%,#2c2a2e 65%,#1d2433 100%)}
.hero-text{left:114px;top:222px;width:500px;font-family:'Titillium Web',sans-serif;font-size:26px;line-height:38px;color:var(--white)}
.btn-start{left:114px;top:403px;width:184px;height:58px;border-radius:29px;background:var(--orange);color:var(--white);display:flex;align-items:center;gap:22px;padding-left:14px;font-family:'Titillium Web',sans-serif;font-weight:600;font-size:17px;box-shadow:0 4px 10px rgba(0,0,0,.3)}

/* audience panels */
.panel{top:570px;width:600px;height:340px;color:var(--white)}
.panel.business{left:0;background:var(--navy)}
.panel.home{left:600px;background:var(--orange)}
.panel h2{position:absolute;top:14px;left:0;width:100%;text-align:center;font-family:'Titillium Web',sans-serif;font-weight:400;font-size:42px}
.panel .rule{position:absolute;top:76px;left:50%;margin-left:-23px;width:46px;height:2px;background:var(--white)}
.panel .thumb{position:absolute;top:111px;width:171px;height:171px;border-radius:50%;background:linear-gradient(160deg,#e8e4d8,#9a9488 60%,#5b5a58)}
.panel p{position:absolute;top:104px;width:245px;font-size:12.5px;line-height:25.5px}
.business .thumb{left:112px}.business p{left:303px}
.home .thumb{left:58px}.home p{left:250px}
.bolt{left:572px;top:696px}

/* section heads */
.sec-title{left:0;width:1200px;text-align:center;font-family:'Titillium Web',sans-serif;font-weight:700;font-size:52px;color:var(--ink)}
.divider{left:566px}
.sec-lead{left:170px;width:860px;text-align:center;font-size:12.5px;line-height:24px;color:var(--muted)}

/* projects */
.project{top:1149px;width:300px;height:300px;border-radius:4px;box-shadow:0 8px 18px rgba(0,0,0,.18)}
.p1{left:0;background:linear-gradient(135deg,#e6e8ec,#9ea3aa 60%,#5e5a55)}
.p2{left:337px;background:linear-gradient(135deg,#e8a73a,#c9801c 60%,#6e4a18)}
.p3{left:677px;background:linear-gradient(160deg,#5a4636,#b59a78 50%,#eee8df)}
.p4{left:1012px;width:188px;border-radius:4px 0 0 4px;background:linear-gradient(150deg,#3a3d40,#c8ccc8 55%,#f2f2ef)}

/* testimonial */
.quote-card{left:224px;top:1662px;width:744px;height:203px;background:var(--white);box-shadow:0 4px 22px rgba(0,0,0,.12)}
.quote-card p{position:absolute;left:40px;top:38px;width:664px;text-align:center;font-size:13.5px;line-height:33px;color:var(--muted)}
.quote-badge{left:241px;top:1667px;width:34px;height:34px;background:var(--pale);color:var(--white);font-family:'Titillium Web',sans-serif;font-weight:700;font-size:40px;line-height:44px;text-align:center}
.quote-tail{left:580px;top:1864px}
.client{left:0;width:1200px;text-align:center}
.client-name{top:1892px;font-size:14px;color:var(--orange)}
.client-role{top:1914px;font-size:12px;color:var(--ink)}
.dots{left:545px;top:1964px;display:flex;gap:11px}
.dots span{width:10px;height:10px;border-radius:50%;background:var(--dot)}
.dots span.on{background:var(--orange)}

/* footer */
.footer-shape{left:0;top:2000px}
.footer-col{top:2137px;color:var(--white)}
.footer-col h3{font-family:'Titillium Web',sans-serif;font-weight:700;font-size:20px;margin-bottom:14px}
.footer-col ul{list-style:none;font-size:12px;font-weight:500}
.footer-col li{height:31px}
.feed{left:110px}
.feed-item{display:flex;gap:12px;height:68px}
.feed-icon{flex:none;width:30px;height:30px;border-radius:50%;background:#4d9fe0;margin-top:3px}
.feed-text{font-size:12px;font-weight:500;line-height:21px}
.feed-text em{color:var(--orange);font-style:normal}
.feed-date{display:block;font-size:9.5px;font-style:italic;line-height:16px}
.services{left:551px}
.company{left:772px}
.footer-brand{left:966px;top:2205px;display:flex;flex-direction:column;align-items:center;gap:8px;color:var(--white)}
.footer-brand .mark{width:52px;height:52px;border-radius:50%;border:3px solid var(--white)}
.footer-brand .name{font-family:'Titillium Web',sans-serif;font-weight:600;font-size:17px;letter-spacing:1px}
.copyright{left:0;top:2420px;width:1200px;height:49px;background:var(--orange);color:var(--white);font-size:13px;display:flex;align-items:center;justify-content:center}
</style>
</head>
<body>

<header>
  <div class="abs topbar">
    <div class="contact phone">
      <svg width="20" height="20" viewBox="0 0 24 24" fill="none" stroke="#fff" stroke-width="1.8"><path d="M5 3h4l2 5-2.5 1.5a11 11 0 0 0 6 6L16 13l5 2v4a2 2 0 0 1-2 2A16 16 0 0 1 3 5a2 2 0 0 1 2-2z"/></svg>
      +1 555 0148
    </div>
    <div class="contact email">
      <svg width="20" height="16" viewBox="0 0 24 18" fill="none" stroke="#fff" stroke-width="1.8"><rect x="1" y="1" width="22" height="16" rx="2"/><path d="M1 2l11 8 11-8"/></svg>
      hello@brightline.example
    </div>
  </div>
  <nav class="abs navbar" aria-label="Main"></nav>
  <div class="abs brand">
    <div class="brand-mark"></div>
    <div class="brand-name">BRIGHTLINE</div>
  </div>
  <ul class="abs menu">
    <li>Home</li><li>Meet the Team</li><li>Our Services</li><li>Projects</li><li>Contact Us</li>
  </ul>
</header>

<section>
  <div class="abs hero" role="img" aria-label="Warm evening interior of a timber-beamed living room lit by pendant lights"></div>
  <p class="abs hero-text">Lorem Ipsum Dolor Sit Amet, Consectetuer Adipiscing Elit, Sed Diam Nonummy Euismod Tincidunt Ut Laoreet Dolore Magna.&nbsp; Se5 Diam Nonummy</p>
  <div class="abs btn-start">
    <svg width="40" height="40" viewBox="0 0 40 40" fill="none" stroke="#5a2a10" stroke-width="3"><path d="M30 14a12 12 0 0 0-21 2"/><path d="M10 26a12 12 0 0 0 21-2"/><path d="M30 7v7h-7"/><path d="M10 33v-7h7"/></svg>
    Get Started
  </div>
</section>

<section>
  <div class="abs panel business">
    <h2>Business</h2><div class="rule"></div>
    <div class="thumb" role="img" aria-label="Open-plan office with ceiling panel lighting"></div>
    <p>Lorem ipsum dolor sit a consectetuer adipiscing elit, sed diam nonum nibh euismod tincidunt ut looreore magna aliquam erat volutpat. Ut wisi enim ad minim veniam, quis nostr exerci tation ullamcorper suscipit loborisl ut aliquip ex ea commodo consequat.</p>
  </div>
  <div class="abs panel home">
    <h2>House Owner</h2><div class="rule"></div>
    <div class="thumb" role="img" aria-label="Lit interior space for a home owner"></div>
    <p>Lorem ipsum dolor sit a consectetuer adipiscing elit, sed diam nonum nibh euismod tincidunt ut looreore magna aliquam erat volutpat. Ut wisi enim ad minim veniam, quis nostr exerci tation ullamcorper suscipit loborisl ut aliquip ex ea commodo consequat.</p>
  </div>
  <svg class="abs bolt" width="56" height="86" viewBox="0 0 56 86"><polygon points="34,0 4,48 24,48 14,86 54,30 32,30 46,0" fill="#fff"/></svg>
</section>

<section>
  <h2 class="abs sec-title" style="top:972px">Our Previous Projects</h2>
  <svg class="abs divider" style="top:1042px" width="68" height="12" viewBox="0 0 68 12"><line x1="0" y1="6" x2="26" y2="6" stroke="#f26a2d"/><line x1="42" y1="6" x2="68" y2="6" stroke="#f26a2d"/><polygon points="36,0 30,7 34,7 32,12 38,5 34,5" fill="#f26a2d"/></svg>
  <p class="abs sec-lead" style="top:1068px">Lorem ipsum dolor sit amet, consectetuer adipiscing elit, sed diam nonummy nib euismod tincidunt ut laoreet dolore magna aliquam erat volutpat. Ut wisi enim ad min veniam, quis nostrud exerci tation ullamcorper suscipit lobortis</p>
  <div class="abs project p1" role="img" aria-label="Project: white ceiling structure with recessed spotlights"></div>
  <div class="abs project p2" role="img" aria-label="Project: golden corridor with perforated backlit wall"></div>
  <div class="abs project p3" role="img" aria-label="Project: lounge with round pendant ceiling lights"></div>
  <div class="abs project p4" role="img" aria-label="Project: bright office with track lighting"></div>
</section>

<section>
  <h2 class="abs sec-title" style="top:1512px">Our Testimonials</h2>
  <svg class="abs divider" style="top:1584px" width="68" height="12" viewBox="0 0 68 12"><line x1="0" y1="6" x2="26" y2="6" stroke="#f26a2d"/><line x1="42" y1="6" x2="68" y2="6" stroke="#f26a2d"/><polygon points="36,0 30,7 34,7 32,12 38,5 34,5" fill="#f26a2d"/></svg>
  <p class="abs sec-lead" style="top:1608px">Lorem ipsum dolor sit amet, consectetuer adipiscing elit, sed diam nonummy nib euismod tincidunt ut laoreet dolore magna.</p>
  <div class="abs quote-card">
    <p>Lorem ipsum dolor sit a con adipiscing elit, sed diam nonum nibismo tincidunt ut laoreore magna aliam erat volutpat. Ut wisi enim ad mini veniam, quis nostr exerci tation ullamorper Lorem ipsum dolor sit a con adipiscing elit, sed diam nonum nibismo tincidunt ut laoreore magna aliam erat volutpat. Ut wisi enim ad mini veniam, quis nostr exerci</p>
  </div>
  <div class="abs quote-badge">&ldquo;</div>
  <svg class="abs quote-tail" width="30" height="14" viewBox="0 0 30 14"><polygon points="0,0 30,0 14,14" fill="#fff"/></svg>
  <p class="abs client client-name">Customer Name</p>
  <p class="abs client client-role">Dolor Nonum Nibismo Tincidunt</p>
  <div class="abs dots"><span class="on"></span><span></span><span></span><span></span></div>
</section>

<footer>
  <svg class="abs footer-shape" width="1200" height="420" viewBox="0 0 1200 420"><polygon points="0,0 362,77 988,0 1200,123 1200,420 0,420" fill="#1f3260"/></svg>
  <div class="abs footer-col feed">
    <h3>Latest Chirpnet</h3>
    <div class="feed-item"><span class="feed-icon"></span><p class="feed-text">Lorem ipsum dolor sit amet, conse adipiscing<br>elit, sed diam <em>nonummy nib euismod</em><span class="feed-date">24th April, 2019</span></p></div>
    <div class="feed-item"><span class="feed-icon"></span><p class="feed-text">Lorem ipsum dolor sit amet, conse adipiscing<br>elit, sed diam <em>nonummy nib euismod</em><span class="feed-date">24th April, 2019</span></p></div>
    <div class="feed-item"><span class="feed-icon"></span><p class="feed-text">Lorem ipsum dolor sit amet, conse adipiscing<br>elit, sed diam <em>nonummy nib euismod</em><span class="feed-date">24th April, 2019</span></p></div>
  </div>
  <div class="abs footer-col services">
    <h3>Services</h3>
    <ul><li>Lorem ipsum</li><li>Dolor sit amet,</li><li>Conse</li><li>Adipiscing</li><li>Lorem ipsum</li><li>Dolor sit amet,</li></ul>
  </div>
  <div class="abs footer-col company">
    <h3>Company</h3>
    <ul><li>Home</li><li>Meet the Team</li><li>Our Services</li><li>Projects</li><li>Contact Us</li></ul>
  </div>
  <div class="abs footer-brand">
    <div class="mark"></div>
    <div class="name">BRIGHTLINE</div>
  </div>
  <div class="abs copyright">© All Rights Reserved. 2019</div>
</footer>

</body>
</html>
```